Letterhead design - Harwick Group

We have just had our Logo created and our now wantng a letterhead design to incorporate this. Please use the same colours as in the logo, which is attached.
Please use the company details below
P O Box 86, Bleneheim 7315
Ph: 03 642 1937
dave@harwickgroup.co.nz
We would like a professional look
We need an overall letterhead design for our varied group of buisinesses which are based in NZ and overseas. We grow and develop buisinesses. Our companies began in NZ but we now have branches overseas as well. People are our greatest asset and we employ some incredible staff. Our buisinesses are scientific, innovative and growing in size and expertise with a financial base.

Target Market(s)

Professionals

Industry/Entity Type

Investment

Requirements
Must have
• Easy to read.
• Please use the same colours as in the logo
• Please use the company details below
• P O Box 86, Bleneheim 7315
• Ph: 03 642 1937
• dave@harwickgroup.co.nz

```html
<!DOCTYPE html>
<html lang="en">
<head>
<meta charset="utf-8">
<title>Harwick Group Letterhead</title>
<link rel="stylesheet" href="https://fonts.googleapis.com/css2?family=Source+Sans+3:wght@400;700&display=swap">
<style>
  :root {
    --brand-green: #0fb26b;
    --brand-grey: #5f6062;
    --paper: #ffffff;
    --backdrop: #ebe8e3;
    --text-light: #ffffff;
  }
  * { box-sizing: border-box; margin: 0; padding: 0; }
  html, body {
    width: 1112px;
    height: 1200px;
    overflow: hidden;
    background: var(--backdrop);
    font-family: "Source Sans 3", Arial, sans-serif;
  }
  .letterhead {
    position: absolute;
    left: 206px;
    top: 104px;
    width: 700px;
    height: 991px;
    background: var(--paper);
    box-shadow: 0 2px 10px rgba(0,0,0,0.12);
  }
  .brand {
    position: absolute;
    top: 44px;
    right: 28px;
    display: flex;
    align-items: center;
    gap: 10px;
  }
  .brand-square {
    width: 40px;
    height: 40px;
    background: var(--brand-grey);
  }
  .brand-name {
    font-weight: 700;
    font-size: 24px;
    letter-spacing: 0.5px;
    text-transform: uppercase;
    color: var(--brand-green);
  }
  .footer-stripe {
    position: absolute;
    left: 0;
    top: 926px;
    width: 100%;
    height: 11px;
    background: var(--brand-green);
  }
  .footer-band {
    position: absolute;
    left: 0;
    top: 945px;
    width: 100%;
    height: 32px;
    background: var(--brand-grey);
  }
  .footer-divider {
    position: absolute;
    left: 93px;
    top: 922px;
    width: 3px;
    height: 59px;
    background: var(--paper);
  }
  .contact {
    position: absolute;
    right: 28px;
    top: 945px;
    height: 32px;
    display: flex;
    align-items: center;
    gap: 6px;
    color: var(--text-light);
    font-size: 14px;
    font-weight: 400;
  }
  .contact-icon {
    width: 15px;
    height: 15px;
    margin-left: 2px;
  }
</style>
</head>
<body>
  <main class="letterhead">
    <header class="brand">
      <span class="brand-square"></span>
      <span class="brand-name">Harwick Group</span>
    </header>

    <div class="footer-stripe"></div>
    <div class="footer-band"></div>
    <div class="footer-divider"></div>

    <footer class="contact">
      <span class="contact-address">P O Box 86, Bleneheim 7315</span>
      <svg class="contact-icon" viewBox="0 0 16 16" aria-hidden="true">
        <circle cx="8" cy="8" r="8" fill="var(--brand-green)"/>
        <path d="M5.2 3.8l1.5 1.6-0.8 1.2c0.5 1.2 1.3 2 2.5 2.6l1.2-0.8 1.6 1.5-0.9 1.5c-2.9-0.4-5.4-2.9-5.8-5.9z" fill="#fff"/>
      </svg>
      <span class="contact-phone">03 642 1937</span>
      <svg class="contact-icon" viewBox="0 0 16 16" aria-hidden="true">
        <circle cx="8" cy="8" r="8" fill="var(--brand-green)"/>
        <rect x="4" y="5.2" width="8" height="5.6" fill="#fff"/>
        <path d="M4 5.2l4 3 4-3" fill="none" stroke="var(--brand-green)" stroke-width="0.9"/>
      </svg>
      <span class="contact-email">dave@harwickgroup.co.nz</span>
    </footer>
  </main>
</body>
</html>
```